Business Card Design Project

I am a Chiropractor that is looking for a new business card.  Our logo was slightly changed lately, therefore need a new, more professional look.
We are a modern, non-stuffy chiropractic office.  Want a contemporary look that will let people know this is not your typical doctors office.  Our logo is red, and contains the name of our business: realign.  The u in the logo is green, stressing the most important part of our business: "u"

Target Market(s)
moderate to upper income bracket, family friendly
www.realignspine-example.com
Gordon Pell
Family Chiropractor
314 Hollis Rd
Bastrop, TX 78999
512.555.0147 phone
512.555.0148 fax
Industry/Entity Type
Business
Requirements
Must have
- www.realignspine-example.com
Gordon Pell
Family Chiropractor
314 Hollis Rd
Bastrop, TX 78999
512.555.0147 phone
512.555.0148 fax

```html
<!DOCTYPE html>
<html lang="en">
<head>
<meta charset="utf-8">
<title>Realign – Business Card</title>
<link rel="stylesheet" href="https://fonts.googleapis.com/css2?family=News+Cycle:wght@400;700&display=swap">
<style>
  :root {
    --lime: #66ff14;
    --red: #ff1f22;
    --white: #ffffff;
    --edge: #b9b9b9;
    --page: #ffffff;
  }
  * { margin: 0; padding: 0; box-sizing: border-box; }
  html, body {
    width: 718px;
    height: 1200px;
    overflow: hidden;
    background: var(--page);
  }
  .card {
    position: absolute;
    left: 24px;
    top: 22px;
    width: 670px;
    height: 1155px;
    border-radius: 54px;
    border: 2px solid var(--edge);
    overflow: hidden;
    background: var(--white);
    font-family: "News Cycle", "Helvetica Neue", Arial, sans-serif;
  }
  .brand-panel {
    position: absolute;
    left: 0; top: 0;
    width: 100%;
    height: 758px;
    background: var(--lime);
  }
  .brand-name {
    position: absolute;
    left: 0; right: 0;
    top: 300px;
    text-align: center;
    font-size: 110px;
    font-weight: 400;
    line-height: 1;
    color: var(--red);
    letter-spacing: 1px;
  }
  .contact-panel {
    position: absolute;
    left: 0; bottom: 0;
    width: 100%;
    height: 363px;
    background: var(--red);
    color: var(--white);
    text-align: center;
  }
  .person-name {
    margin-top: 24px;
    font-size: 31px;
    font-weight: 700;
    line-height: 40px;
  }
  .person-title {
    font-size: 33px;
    font-weight: 400;
    line-height: 44px;
  }
  .address {
    margin-top: 12px;
    font-style: normal;
    font-size: 28px;
    line-height: 40px;
  }
  .website {
    margin-top: 20px;
    font-size: 24px;
    font-weight: 700;
    line-height: 32px;
  }
</style>
</head>
<body>
  <div class="card">
    <section class="brand-panel">
      <div class="brand-name">realign</div>
    </section>
    <section class="contact-panel">
      <p class="person-name">Gordon Pell</p>
      <p class="person-title">Family Chiropractor</p>
      <address class="address">
        314 Hollis Rd<br>
        Bastrop, TX 78999<br>
        Phone: 512.555.0147<br>
        Fax: 512.555.0148
      </address>
      <p class="website">www.realignspine-example.com</p>
    </section>
  </div>
</body>
</html>
```